Agriculture Business Card

I want to use my existing logo and use my tagline of "Don't Guess...Soil Test" on the card. Looking for a double sided card that will really get peoples attention.
Contact Info:
Brisco Harvest Crop Solutions
Calvin Brisco
2917 K Lane
Otoe, NE 68539
402-815-2493
calvin.r.brisco@furrowpost.net

```html
<!DOCTYPE html>
<html lang="en">
<head>
<meta charset="utf-8">
<title>Brisco Harvest Crop Solutions – Business Card</title>
<link rel="stylesheet" href="https://fonts.googleapis.com/css2?family=Arimo:wght@400;700&display=swap">
<style>
  :root {
    --backdrop: #e9e9e7;
    --card-white: #ffffff;
    --card-dark: #2b2b2b;
    --leaf-green: #2eaa45;
    --earth-brown: #8a4a2c;
    --corn-gold: #f4a81d;
    --ink-grey: #555555;
    --rule-grey: #8c8c8c;
    --emboss-grey: #8e8e8e;
  }
  * { box-sizing: border-box; margin: 0; padding: 0; }
  html, body {
    width: 1200px; height: 802px; overflow: hidden;
    background: var(--backdrop);
    font-family: "Arimo", Arial, sans-serif;
  }
  .sheet {
    width: 1200px; height: 802px;
    display: flex; flex-direction: column;
    align-items: center; justify-content: center; gap: 30px;
  }
  .card {
    position: relative;
    width: 620px; height: 354px;
    box-shadow: 0 6px 18px rgba(0,0,0,0.18);
  }
  /* Front side */
  .card-front { background: var(--card-white); }
  .brand {
    position: absolute; right: 46px; top: 58px;
    display: flex; align-items: center; gap: 14px;
  }
  .brand-mark {
    width: 34px; height: 34px; border-radius: 50%;
    background: var(--corn-gold);
  }
  .brand-name {
    font-weight: 700; font-size: 25px; line-height: 1.15;
    color: var(--earth-brown); text-align: right;
    width: 250px;
  }
  .rule {
    position: absolute; left: 40px; right: 40px; top: 214px;
    height: 1px; background: var(--rule-grey);
  }
  .holder-name {
    position: absolute; left: 40px; top: 180px;
    font-size: 26px; font-weight: 400; letter-spacing: 0.5px;
    color: var(--leaf-green); text-transform: uppercase;
  }
  .contact {
    position: absolute; left: 40px; top: 230px;
    list-style: none; font-size: 15px; color: var(--ink-grey);
    line-height: 1.55;
  }
  .contact li { display: flex; align-items: center; gap: 8px; }
  .contact svg { width: 14px; height: 14px; fill: var(--leaf-green); flex: none; }
  .address {
    position: absolute; right: 40px; top: 230px;
    font-style: normal; font-size: 15px; color: var(--ink-grey);
    line-height: 1.55; text-align: left;
  }
  /* Back side */
  .card-back {
    background: var(--card-dark);
    display: flex; flex-direction: column;
    align-items: center; justify-content: center;
  }
  .back-brand { display: flex; align-items: center; gap: 14px; margin-top: -10px; }
  .back-brand .brand-mark { background: #3a3a3a; width: 40px; height: 40px; }
  .back-brand .brand-name {
    color: var(--emboss-grey); width: auto; text-align: center;
    font-size: 27px;
  }
  .tagline {
    margin-top: 46px;
    font-weight: 700; font-size: 19px; letter-spacing: 0.3px;
    color: var(--corn-gold);
  }
</style>
</head>
<body>
<main class="sheet">
  <section class="card card-front" aria-label="Business card front">
    <div class="brand">
      <span class="brand-mark"></span>
      <div class="brand-name">Brisco Harvest<br>Crop Solutions</div>
    </div>
    <h1 class="holder-name">Calvin Brisco</h1>
    <div class="rule"></div>
    <ul class="contact">
      <li>
        <svg viewBox="0 0 24 24" aria-hidden="true"><path d="M6.6 10.8a15.1 15.1 0 0 0 6.6 6.6l2.2-2.2a1 1 0 0 1 1-.25 11.4 11.4 0 0 0 3.6.57 1 1 0 0 1 1 1V20a1 1 0 0 1-1 1A17 17 0 0 1 3 4a1 1 0 0 1 1-1h3.5a1 1 0 0 1 1 1c0 1.25.2 2.45.57 3.6a1 1 0 0 1-.25 1z"/></svg>
        402-815-2493
      </li>
      <li>
        <svg viewBox="0 0 24 24" aria-hidden="true"><path d="M2 5h20v14H2z M4 7v.4l8 5.1 8-5.1V7z" fill-rule="evenodd"/></svg>
        calvin.r.brisco@furrowpost.net
      </li>
    </ul>
    <address class="address">2917 K Lane<br>Otoe, NE 68539</address>
  </section>

  <section class="card card-back" aria-label="Business card back">
    <div class="back-brand">
      <span class="brand-mark"></span>
      <div class="brand-name">Brisco Harvest<br>Crop Solutions</div>
    </div>
    <p class="tagline">Don't Guess...Soil Test</p>
  </section>
</main>
</body>
</html>
```